Veteran Owned General Contractor needs Bold New Business Cards

We are a service disabled veteran owned small business. We're a general contractor that specializes in excavation, underground utilities, site work, land clearing and demolition. We would like a fresh, simple, bold, new look for our business cards. We're open to ideas! We'd like to incorporate the following information on the card:

Company Name & Logo, Name of Person, Job Title, Office Phone, Fax, Cell Phone, Email Address, Website, SDVOSB

Our logo is included. We look forward to your thoughts.

Thank you!

Reason: Hello Due to the overwhelming response to this project, we are extending the deadline one time to allow for improved communication and feedback with the top candidates. We would like to thank everyone for their hard work and exceptional creativity! Thank you

Industry/Entity Type

Business

Contact Information for Business Card

Font styles to use
Sans Serif

Requirements
Nice to have
• As we are a veteran owned company, it would be nice to incorporate an American flag into the design. Maybe on the back?

```html
<!DOCTYPE html>
<html lang="en">
<head>
<meta charset="utf-8">
<title>Bedrock7 Business Card</title>
<link rel="stylesheet" href="https://fonts.googleapis.com/css2?family=Oswald:wght@500&family=Open+Sans:wght@400;700;800&display=swap">
<style>
  :root {
    --page: #e9e6e1;
    --card: #161616;
    --green: #6cc04a;
    --grey-text: #b5b5b5;
    --grey-line: #8a8a8a;
    --mark: #8c8c8c;
  }
  * { margin: 0; padding: 0; box-sizing: border-box; }
  html, body { width: 1200px; height: 1000px; overflow: hidden; background: var(--page); }
  .canvas { position: relative; width: 1200px; height: 1000px; }
  .card {
    position: absolute; left: 267px; width: 665px; height: 396px;
    border-radius: 28px; overflow: hidden; background: var(--card);
  }
  .card--front { top: 75px; }
  .card--back { top: 534px; }

  .identity { position: absolute; right: 357px; top: 244px; text-align: right; }
  .identity__name {
    font-family: "Oswald", sans-serif; font-weight: 500; font-size: 31px;
    color: var(--green); letter-spacing: 0.5px; line-height: 1;
  }
  .identity__title {
    font-family: "Open Sans", sans-serif; font-size: 16px; color: var(--grey-text);
    margin-top: 4px;
  }
  .divider { position: absolute; left: 331px; top: 160px; width: 2px; height: 78px; background: var(--grey-line); }

  .contact { position: absolute; left: 356px; top: 151px; list-style: none; }
  .contact__item {
    display: flex; align-items: center; gap: 6px; height: 22.5px;
    font-family: "Open Sans", sans-serif; font-size: 16px; color: var(--grey-text);
  }
  .contact__icon { width: 14px; height: 14px; fill: var(--green); flex: none; }

  .address {
    position: absolute; left: 0; right: 0; top: 347px; text-align: center;
    font-family: "Open Sans", sans-serif; font-size: 15.5px; color: var(--grey-text);
  }
  .address__brand { color: var(--green); font-weight: 700; }

  .flag-field {
    position: absolute; inset: 0;
    background:
      linear-gradient(180deg, rgba(30,30,30,0.55), rgba(30,30,30,0.55)),
      linear-gradient(115deg, #3b3d48 0%, #3b3d48 38%, #5a3a3a 38%, #4a4a4a 52%, #5a3a3a 66%, #4a4a4a 80%, #5a3a3a 100%);
  }
  .brand-square {
    position: absolute; left: 283px; top: 94px; width: 100px; height: 100px;
    border-radius: 14px; background: var(--mark);
  }
  .brand-name {
    position: absolute; left: 0; right: 0; top: 222px; text-align: center;
    font-family: "Open Sans", sans-serif; font-weight: 800; font-size: 60px;
    letter-spacing: 4px; color: var(--green); line-height: 1;
  }
</style>
</head>
<body>
<main class="canvas">
  <section class="card card--front">
    <div class="identity">
      <div class="identity__name">DANA HOLBROOK</div>
      <div class="identity__title">Vice President</div>
    </div>
    <div class="divider"></div>
    <ul class="contact">
      <li class="contact__item">
        <svg class="contact__icon" viewBox="0 0 16 16"><path d="M1 5c0-2 3-3 7-3s7 1 7 3v1h-4V5H5v1H1zM3 8h10l1 6H2z"/></svg>
        <span>+ 000 000 0000</span>
      </li>
      <li class="contact__item">
        <svg class="contact__icon" viewBox="0 0 16 16"><path d="M4 1h8v4H4zM1 6h14v6h-3v3H4v-3H1zM5 10v4h6v-4z"/></svg>
        <span>+ 000 000 0000</span>
      </li>
      <li class="contact__item">
        <svg class="contact__icon" viewBox="0 0 16 16"><path d="M1 3h14v10H1zM2 4l6 5 6-5z" fill-rule="evenodd"/></svg>
        <span>info@bedrock7builders.com</span>
      </li>
      <li class="contact__item">
        <svg class="contact__icon" viewBox="0 0 16 16"><circle cx="8" cy="8" r="7"/><path d="M1 8h14M8 1c3 3 3 11 0 14M8 1c-3 3-3 11 0 14" stroke="#161616" stroke-width="1.2" fill="none"/></svg>
        <span>www.bedrock7builders.com</span>
      </li>
    </ul>
    <p class="address"><span class="address__brand">BEDROCK7</span> - Box 2460 4810- 48 Ave Stony Ridge, AB T7R 2K5</p>
  </section>

  <section class="card card--back">
    <div class="flag-field" role="img" aria-label="Waving American flag photograph, darkened"></div>
    <div class="brand-square"></div>
    <div class="brand-name">BEDROCK7</div>
  </section>
</main>
</body>
</html>
```